Business card for my new company (Accounting firm)

I need a business card for my new business Corvel Advisory and Finance SA. Our services are accounting, tax, audit and financial management. Our customers are small companies, start-ups and new companies. The final design has to show financial security, trust and growth. Please find our logo attached to the business card. Text for the business card: Corvel Advisory and Finance SA Tomas de Valbueno Director and Founder Certified Accountant Tel. 022 418 27 53 tv@corvelconseil.ch www.corvelconseil.ch Rue des Verniquets 14 1201 Geneva
Target Market(s)
Our customers are small companies, start-ups and new companies.
Industry/Entity Type
Finance And Accounting
Contact Information for Business Card
Corvel Conseil et Finance SA
Tomas de Valbueno
Directeur et Fondateur
Expert-comptable diplômé
Tél. 022 418 27 53
tv@corvelconseil.ch
www.corvelconseil.ch
Rue des Verniquets 14
1201 Genève

```html
<!DOCTYPE html>
<html lang="fr">
<head>
<meta charset="utf-8">
<title>Talvore Conseil et Finance — Carte de visite</title>
<link rel="stylesheet" href="https://fonts.googleapis.com/css2?family=Poppins:wght@400;500;600&display=swap">
<style>
  :root {
    --backdrop: #a7a8a9;
    --paper: #eeeff1;
    --ink: #2f3236;
    --ink-soft: #45484c;
    --blue-deep: #17588b;
    --blue-mid: #1d7bbd;
    --blue-light: #2a9fd4;
    --silver: #e3e6e9;
  }
  * { box-sizing: border-box; margin: 0; padding: 0; }
  html, body {
    width: 1105px; height: 1200px; overflow: hidden;
    background: var(--backdrop);
    font-family: "Poppins", sans-serif;
  }
  .canvas { position: relative; width: 1105px; height: 1200px; }

  .card { position: absolute; left: 182px; width: 748px; height: 427px; }
  .card--front { top: 118px; background: var(--paper); }
  .card--back {
    top: 635px; height: 428px;
    background: linear-gradient(90deg, var(--blue-light) 0%, #1f84c2 45%, var(--blue-deep) 100%);
  }

  .brand { position: absolute; text-align: center; font-weight: 600; }
  .brand__mark { display: block; margin: 0 auto; }
  .brand__name { display: block; line-height: 1; letter-spacing: 2px; }
  .brand__tagline { display: block; font-size: 13px; font-weight: 500; letter-spacing: 1.6px; line-height: 1; }

  .card--front .brand { right: 38px; top: 76px; width: 180px; color: var(--ink); }
  .card--front .brand__mark { width: 72px; height: 72px; background: var(--blue-mid); margin-bottom: 14px; }
  .card--front .brand__name { font-size: 42px; }
  .card--front .brand__tagline { margin-top: 8px; }

  .card--back .brand { left: 0; right: 0; top: 130px; color: var(--silver); }
  .card--back .brand__mark { width: 90px; height: 90px; background: var(--silver); margin-bottom: 30px; }
  .card--back .brand__name { font-size: 46px; }
  .card--back .brand__tagline { margin-top: 10px; }

  .person { position: absolute; left: 39px; top: 218px; color: var(--ink); }
  .person__name { font-size: 24px; font-weight: 500; line-height: 30px; }
  .person__role { font-size: 16.5px; line-height: 20px; color: var(--ink-soft); }

  .divider { position: absolute; left: 39px; right: 44px; top: 302px; display: flex; gap: 3px; }
  .divider span { flex: 1; height: 3px; }
  .divider span:nth-child(1) { background: var(--blue-deep); }
  .divider span:nth-child(2) { background: var(--blue-mid); }
  .divider span:nth-child(3) { background: var(--blue-light); }

  .contact, .address {
    position: absolute; top: 320px; font-style: normal;
    font-size: 17px; line-height: 21px; color: var(--ink-soft);
  }
  .contact { left: 39px; }
  .address { right: 44px; text-align: right; }
</style>
</head>
<body>
<main class="canvas">
  <section class="card card--front" aria-label="Recto de la carte">
    <div class="brand">
      <span class="brand__mark"></span>
      <span class="brand__name">TALVORE</span>
      <span class="brand__tagline">CONSEIL ET FINANCE</span>
    </div>
    <div class="person">
      <p class="person__name">Tomas de Valbueno</p>
      <p class="person__role">Directeur et Fondateur</p>
      <p class="person__role">Expert-comptable diplômé</p>
    </div>
    <div class="divider"><span></span><span></span><span></span></div>
    <address class="contact">
      Tél. 022 418 27 53<br>
      tv@corvelconseil.ch<br>
      www.corvelconseil.ch
    </address>
    <address class="address">
      Corvel Conseil et Finance SA<br>
      Rue des Verniquets 14<br>
      1201 Genève
    </address>
  </section>

  <section class="card card--back" aria-label="Verso de la carte">
    <div class="brand">
      <span class="brand__mark"></span>
      <span class="brand__name">TALVORE</span>
      <span class="brand__tagline">CONSEIL ET FINANCE</span>
    </div>
  </section>
</main>
</body>
</html>
```